Create look and feel for existing Web Page

Update Web Page

We have a website at http://www.usekivra.com/index-web.html. It is a single page html site, with a custom signup form. We also have a quill bay plugin at the bottom of the page. We'd like to redesign the look and feel of the entire site. We sell software to eye doctors. Also called optometrists, our software tool makes it easy for doctors to manage patients, bill, and document patient encounters. I have included our logos below.

We are looking for a new design preferably in HTML 5, CSS etc. The fields on the form on this page: http://www.usekivra.com/index-web.html

You can get screen shots of our software application at this site: http://staging.usekivra.com
username: test@samplevora.com
password: password

```html
<!DOCTYPE html>
<html lang="en">
<head>
<meta charset="utf-8">
<title>Iralune – Optometry Practice Software</title>
<link rel="stylesheet" href="https://fonts.googleapis.com/css2?family=Montserrat:wght@400;500;600;700;800&family=Poppins:wght@600;700&display=swap">
<style>
  :root {
    --orange: #f7931e;
    --orange-deep: #f15a24;
    --orange-light: #fbb03b;
    --green: #39b54a;
    --green-dark: #22913a;
    --white: #ffffff;
    --gray-row: #e3e3e3;
    --ink: #4d4d4d;
    --ink-soft: #7a7a7a;
  }
  * { box-sizing: border-box; margin: 0; padding: 0; }
  html, body { width: 1200px; height: 2684px; overflow: hidden; }
  body { font-family: "Montserrat", sans-serif; color: var(--white); background: var(--white); position: relative; }
  section, header, footer { position: absolute; left: 0; width: 1200px; }
  .wave { position: absolute; left: 0; width: 1200px; display: block; }

  /* Hero */
  .hero { top: 0; height: 640px; background: linear-gradient(180deg, var(--orange) 0%, #f7871e 100%); }
  .brand { font-family: "Montserrat", sans-serif; font-weight: 700; font-size: 58px; letter-spacing: 1px; color: var(--white); position: absolute; line-height: 1; }
  .hero .brand { left: 190px; top: 12px; }
  .nav { position: absolute; right: 192px; top: 44px; display: flex; gap: 30px; font-size: 14px; font-weight: 500; }
  .device { position: absolute; left: 230px; top: 120px; width: 380px; height: 420px; border-radius: 36px;
    background: linear-gradient(150deg, #e9e2d8 0%, #3c4a5c 45%, #e9b38f 100%); }
  .hero-copy { position: absolute; left: 660px; top: 172px; width: 380px; }
  .eyebrow { font-size: 24px; font-weight: 500; }
  .hero-copy h1 { font-size: 40px; font-weight: 700; line-height: 1.15; margin-top: 6px; }
  .hero-copy p { font-size: 13px; line-height: 1.55; margin-top: 18px; width: 330px; }
  .btn { display: inline-block; background: var(--green); color: var(--white); font-size: 13px; font-weight: 600;
    border-radius: 4px; padding: 12px 24px; }
  .hero-copy .btn { margin-top: 22px; }

  /* Features */
  .features { top: 540px; height: 700px; background: linear-gradient(180deg, #f7881f 0%, var(--orange-deep) 100%); }
  .features-intro { position: absolute; left: 160px; top: 110px; width: 320px; }
  .features-intro h2 { font-family: "Poppins", sans-serif; font-size: 34px; font-weight: 700; line-height: 1.22; }
  .features-intro p { font-size: 13px; line-height: 1.5; margin-top: 20px; width: 290px; }
  .divider { position: absolute; left: 500px; top: 114px; width: 1px; height: 370px; background: rgba(255,255,255,.6); }
  .feature { position: absolute; width: 240px; }
  .feature h3 { font-size: 20px; font-weight: 700; letter-spacing: 1px; }
  .feature p { font-size: 12px; line-height: 1.45; margin-top: 6px; }

  /* Pricing */
  .pricing { top: 1240px; height: 760px; }
  .pricing h2 { position: absolute; width: 100%; top: 86px; text-align: center; color: var(--ink); font-size: 36px; font-weight: 500; letter-spacing: 2px; }
  .free-card { position: absolute; left: 228px; top: 180px; width: 272px; height: 420px; border-radius: 8px;
    background: linear-gradient(180deg, var(--orange) 0%, var(--orange-deep) 100%); text-align: center; padding-top: 36px; }
  .free-card .label { font-size: 40px; font-weight: 700; letter-spacing: 2px; }
  .free-card .amount { font-size: 92px; font-weight: 700; line-height: 1; margin-top: 4px; }
  .free-card p { font-size: 15px; line-height: 1.45; margin: 18px auto 0; width: 210px; }
  .free-card .btn { margin-top: 40px; font-size: 12px; }
  .plan { position: absolute; left: 520px; width: 468px; height: 94px; background: var(--gray-row); border-radius: 4px; }
  .plan-info { position: absolute; left: 36px; top: 26px; width: 230px; color: var(--ink); }
  .plan-info strong { font-size: 14px; font-weight: 600; display: block; }
  .plan-info span { font-size: 11px; color: var(--ink-soft); line-height: 1.35; display: block; margin-top: 3px; }
  .price-tag { position: absolute; right: 0; top: 0; width: 176px; height: 94px; }
  .price { position: absolute; right: 12px; top: 18px; text-align: left; white-space: nowrap; }
  .price b { font-size: 34px; font-weight: 700; }
  .price small { font-size: 14px; font-weight: 600; }
  .price em { display: block; font-style: normal; font-size: 11px; margin-top: -2px; }
  .all-plan { position: absolute; left: 228px; top: 592px; width: 760px; height: 88px; background: var(--green); border-radius: 4px; }
  .all-plan .text { position: absolute; left: 24px; top: 32px; font-size: 17px; font-weight: 600; }
  .all-plan .price-box { position: absolute; right: 0; top: 0; width: 144px; height: 88px; background: var(--green-dark); border-radius: 0 4px 4px 0; }
  .all-plan .price { right: 12px; top: 16px; }

  /* Signup */
  .signup { top: 1960px; height: 620px; background: linear-gradient(180deg, var(--orange) 0%, var(--orange-deep) 100%); }
  .signup-copy { position: absolute; left: 260px; top: 260px; width: 320px; }
  .signup-copy h2 { font-family: "Poppins", sans-serif; font-size: 36px; font-weight: 700; line-height: 1.2; }
  .signup-copy p { font-size: 12px; line-height: 1.5; margin-top: 18px; width: 300px; }
  .signup-form { position: absolute; left: 640px; top: 264px; width: 300px; }
  .field { height: 36px; background: var(--white); border-radius: 3px; margin-bottom: 8px; color: #aaa; font-size: 12px; padding: 10px 12px; }
  .signup-form .btn { margin-top: 10px; font-size: 12px; }

  /* Footer */
  .footer { top: 2564px; height: 120px; background: var(--orange-deep); }
  .footer .nav { left: 190px; right: auto; top: 52px; }
  .footer .brand { right: 190px; top: 28px; }
</style>
</head>
<body>

<header class="hero">
  <div class="brand">iralune</div>
  <nav class="nav"><span>Home</span><span>Products</span><span>Pricing</span><span>Sign Up</span></nav>
  <div class="device" role="img" aria-label="Hand holding a smartphone showing the Iralune charting app"></div>
  <div class="hero-copy">
    <div class="eyebrow">Lease Practices:</div>
    <h1>Choose How You Spend Your Time</h1>
    <p>Spend less time on charting, paperwork and billing. Give your staff the tools to automate the busy work of the office and put time back with your patients.</p>
    <span class="btn">Get FREE Charting Tool</span>
  </div>
</header>

<section class="features">
  <svg class="wave" style="top:-2px" height="120" viewBox="0 0 1200 120" preserveAspectRatio="none"><path d="M0 0 H1200 V40 C1000 120 760 20 560 70 C380 115 180 60 0 90 Z" fill="#f7871e"/></svg>
  <div class="features-intro">
    <h2>AI TO AUTOMATE OPTOMETRY OFFICE TASKS</h2>
    <p>Iralune uses AI to automate, assist and streamline the daily tasks of optometry offices so you can do what you love.</p>
  </div>
  <div class="divider"></div>
  <div class="feature" style="left:520px;top:110px"><h3>SCHEDULE</h3><p>Patients book online and reminders go out for you, around the clock.</p></div>
  <div class="feature" style="left:520px;top:230px"><h3>BILL</h3><p>Claims are built from the chart and sent with one click.</p></div>
  <div class="feature" style="left:520px;top:350px"><h3>INTAKE</h3><p>Forms are filled before the visit and flow into the record.</p></div>
  <div class="feature" style="left:812px;top:110px"><h3>ELIGIBLE</h3><p>Insurance is checked ahead of each visit, with no phone calls.</p></div>
  <div class="feature" style="left:812px;top:230px"><h3>REVIEW</h3><p>Happy patients are asked for reviews that grow your practice.</p></div>
  <div class="feature" style="left:812px;top:350px"><h3>CHART</h3><p>Findings are charted fast with smart templates built for the eye exam.</p></div>
  <svg class="wave" style="bottom:-2px" height="140" viewBox="0 0 1200 140" preserveAspectRatio="none"><path d="M0 90 C220 20 420 130 640 70 C860 10 1020 100 1200 40 V140 H0 Z" fill="#ffffff"/></svg>
</section>

<section class="pricing">
  <h2>PRICING</h2>
  <div class="free-card">
    <div class="label">FREE</div>
    <div class="amount">$0</div>
    <p>Chart patient findings for FREE. Unlimited users, doctors, and locations.</p>
    <span class="btn">Get FREE Charting Tool</span>
  </div>

  <div class="plan" style="top:184px">
    <div class="plan-info"><strong>Pick 1 Add-on</strong><span>Choose one feature: schedule, intake, bill, eligible or review</span></div>
    <svg class="price-tag" viewBox="0 0 176 94"><path d="M40 0 H172 a4 4 0 0 1 4 4 V90 a4 4 0 0 1 -4 4 H0 Z" fill="#39b54a"/></svg>
    <div class="price"><b>$99</b><small>/mo</small><em>per location</em></div>
  </div>
  <div class="plan" style="top:288px">
    <div class="plan-info"><strong>Pick 2 Add-ons</strong><span>Choose any two features: schedule, intake, bill, eligible or review</span></div>
    <svg class="price-tag" viewBox="0 0 176 94"><path d="M40 0 H172 a4 4 0 0 1 4 4 V90 a4 4 0 0 1 -4 4 H0 Z" fill="#39b54a"/></svg>
    <div class="price"><b>$189</b><small>/mo</small><em>per location</em></div>
  </div>
  <div class="plan" style="top:392px">
    <div class="plan-info"><strong>Pick 3 Add-ons</strong><span>Choose any three features: schedule, intake, bill, eligible or review</span></div>
    <svg class="price-tag" viewBox="0 0 176 94"><path d="M40 0 H172 a4 4 0 0 1 4 4 V90 a4 4 0 0 1 -4 4 H0 Z" fill="#39b54a"/></svg>
    <div class="price"><b>$279</b><small>/mo</small><em>per location</em></div>
  </div>
  <div class="plan" style="top:496px">
    <div class="plan-info"><strong>Pick 4 Add-ons</strong><span>Choose any four features: schedule, intake, bill, eligible or review</span></div>
    <svg class="price-tag" viewBox="0 0 176 94"><path d="M40 0 H172 a4 4 0 0 1 4 4 V90 a4 4 0 0 1 -4 4 H0 Z" fill="#39b54a"/></svg>
    <div class="price"><b>$369</b><small>/mo</small><em>per location</em></div>
  </div>

  <div class="all-plan">
    <div class="text">Get all features : schedule, intake, bill, eligible and review</div>
    <div class="price-box"></div>
    <div class="price"><b>$459</b><small>/mo</small><em>per location</em></div>
  </div>
</section>

<section class="signup">
  <svg class="wave" style="top:-2px" height="160" viewBox="0 0 1200 160" preserveAspectRatio="none"><path d="M0 0 H1200 V70 C1000 10 820 120 600 90 C380 60 200 10 0 60 Z" fill="#ffffff"/></svg>
  <div class="signup-copy">
    <h2>GET STARTED WITH A FREE CHARTING TOOL</h2>
    <p>Sign up in minutes and start charting today. No credit card required, and add features whenever you are ready.</p>
  </div>
  <form class="signup-form">
    <div class="field">Full Name</div>
    <div class="field">Email</div>
    <div class="field">Phone</div>
    <div class="field">Practice Name</div>
    <div class="field">Locations</div>
    <span class="btn">Get FREE Charting Tool</span>
  </form>
</section>

<footer class="footer">
  <nav class="nav"><span>Home</span><span>Products</span><span>Pricing</span><span>Sign Up</span></nav>
  <div class="brand">iralune</div>
</footer>

</body>
</html>
```